Saucy Velvet Impz Business Card

We need business cards designed for our consultants to use and hand out to customers.
We are an Adult party plan company (like Crelvaware but sex toys and lingerie)
We would like bright colours pinks, purples.
The cards need our logo
Space for the reps phone number email address and name.
We need our website on it www.saucyvelvetimps.com.au

```html
<!DOCTYPE html>
<html lang="en">
<head>
<meta charset="utf-8">
<title>Saucy Velvet Impz – Business Card</title>
<link href="https://fonts.googleapis.com/css2?family=Quicksand:wght@400;500;700&display=swap" rel="stylesheet">
<style>
  :root {
    --stage: #e9e4dc;
    --card: #0b0b0c;
    --card-edge: #1a1a1c;
    --pink: #e8308f;
    --silhouette: #23272b;
    --text-light: #d9d9d9;
    --smoke: #5a5d62;
  }
  * { box-sizing: border-box; margin: 0; padding: 0; }
  html, body {
    width: 1200px; height: 920px; overflow: hidden;
    background: var(--stage);
    font-family: "Quicksand", sans-serif;
  }
  .stage {
    position: relative; width: 1200px; height: 920px;
    display: flex; justify-content: center; align-items: center; gap: 60px;
  }
  .card {
    position: relative; width: 340px; height: 600px;
    background: var(--card);
    border: 1px solid var(--card-edge);
    box-shadow: 0 18px 40px rgba(0,0,0,.28);
    overflow: hidden;
  }
  /* back side */
  .card-back .figure-art {
    position: absolute; left: 40px; top: 70px; width: 170px; height: 480px;
    background: var(--silhouette);
    border-radius: 80px 80px 30px 30px;
    opacity: .9;
  }
  .card-back .brand-vertical {
    position: absolute; right: 34px; top: 40px;
    writing-mode: vertical-rl;
    color: var(--pink);
    font-size: 24px; font-weight: 400;
    letter-spacing: 22px;
  }
  /* front side */
  .card-front .brand {
    position: absolute; left: 30px; top: 44px;
    display: flex; align-items: center; gap: 12px;
  }
  .brand-dot { width: 34px; height: 34px; border-radius: 50%; background: var(--pink); }
  .brand-name { color: var(--pink); font-size: 24px; font-weight: 500; }
  .rep-name {
    position: absolute; left: 30px; top: 132px;
    color: var(--pink); font-size: 26px; font-weight: 700;
  }
  .contact-list {
    position: absolute; left: 30px; top: 186px;
    list-style: none; color: var(--text-light);
    font-size: 15px; font-weight: 400;
  }
  .contact-list li { display: flex; align-items: center; gap: 10px; height: 30px; }
  .contact-list .icon { width: 16px; height: 16px; flex: none; }
  .contact-list .website { padding-left: 0; }
  .smoke-art {
    position: absolute; left: 0; right: 0; bottom: 0; height: 300px;
    background: radial-gradient(ellipse at 45% 60%, rgba(90,93,98,.55), rgba(11,11,12,0) 65%);
  }
</style>
</head>
<body>
<main class="stage">
  <section class="card card-back" aria-label="Card back">
    <div class="figure-art" role="img" aria-label="Faint dark silhouette of a seated woman with devil horns"></div>
    <p class="brand-vertical">Saucy Velvet Impz</p>
  </section>

  <section class="card card-front" aria-label="Card front">
    <div class="brand">
      <span class="brand-dot"></span>
      <span class="brand-name">Saucy Velvet Impz</span>
    </div>
    <h1 class="rep-name">Your Name</h1>
    <ul class="contact-list">
      <li>
        <svg class="icon" viewBox="0 0 16 16"><circle cx="8" cy="8" r="8" fill="var(--pink)"/><path d="M5 4.5l1.6-.3.8 2-1 .8a6 6 0 0 0 2.6 2.6l.8-1 2 .8-.3 1.6c-3.4.4-6.9-3.1-6.5-6.5z" fill="#0b0b0c"/></svg>
        <span>0400 555 271</span>
      </li>
      <li>
        <svg class="icon" viewBox="0 0 16 16"><circle cx="8" cy="8" r="8" fill="var(--pink)"/><rect x="4" y="5" width="8" height="6" rx="1" fill="#0b0b0c"/><path d="M4.3 5.4L8 8.3l3.7-2.9" stroke="var(--pink)" fill="none" stroke-width="1"/></svg>
        <span>info@saucyvelvetimps.com.au</span>
      </li>
      <li>
        <svg class="icon" viewBox="0 0 16 16"><circle cx="8" cy="8" r="8" fill="var(--pink)"/><path d="M5.5 4l6 4-2.6.5 1.4 2.8-1 .5-1.4-2.8L6 10.8z" fill="#0b0b0c"/></svg>
        <span>www.saucyvelvetimps.com.au</span>
      </li>
      <li class="website"><span>www.saucyvelvetimps.com.au</span></li>
    </ul>
    <div class="smoke-art" role="img" aria-label="Wisps of grey smoke rising from the bottom of the card"></div>
  </section>
</main>
</body>
</html>
```